Branding website for a Data Science company with 1 product

Branding website for a Data Science company, featuring our main product: Lumoria. The purpose of the website is to get potential clients to get a peek at what we do, but the main purpose is to get them to get in touch with us. The website will not answer all questions. Therefore the contact details and contact form is a must-have .

Target Market(s)

Potential new B2B clients with medium to large websites, application users (behind a login)

Industry/Entity Type

It Company

Coding

Coded - Design and coding required

Number of Pages Required

2 page

Font styles to use
Sans Serif

Colors

Designer to choose colors to be used in the design.

Requirements
Must have
• A contact form and branding a product

```html
<!DOCTYPE html>
<html lang="en">
<head>
<meta charset="utf-8">
<title>Quantil Partners — Data Science</title>
<link rel="stylesheet" href="https://fonts.googleapis.com/css2?family=Jost:wght@300;400;500&family=PT+Sans:wght@400;700&display=swap">
<style>
:root{
  --orange:#f05a28;
  --orange-deep:#e2511f;
  --ink:#555;
  --ink-soft:#666;
  --grey-btn:#7b7b7b;
  --grey-icon:#6f6f6f;
  --page:#ffffff;
  --panel:#f2f2f2;
  --line:#cfcfcf;
  --white:#fff;
}
*{margin:0;padding:0;box-sizing:border-box}
html,body{width:1200px;height:2624px;overflow:hidden;background:var(--page)}
body{position:relative;font-family:"PT Sans",Arial,sans-serif;color:var(--ink)}
.abs{position:absolute}

/* header */
.site-header{position:absolute;left:0;top:0;width:1200px;height:126px;background:var(--white)}
.brand{position:absolute;left:78px;top:34px;display:flex;align-items:center;gap:16px}
.brand-dot{width:52px;height:52px;border-radius:50%;background:var(--orange)}
.brand-name{font-family:"Jost",sans-serif;font-weight:400;font-size:44px;letter-spacing:3px;color:var(--orange);text-transform:uppercase;line-height:1}
.main-nav a{position:absolute;top:52px;font-size:15px;color:#666;text-decoration:none;text-transform:uppercase;letter-spacing:.3px}
.main-nav a.active{color:var(--orange)}
.nav-underline{position:absolute;left:618px;top:80px;width:74px;height:4px;border-radius:2px;background:linear-gradient(90deg,#ddd,#888,#ddd)}

/* hero */
.hero{position:absolute;left:0;top:126px;width:1200px;height:570px;box-shadow:0 10px 14px rgba(0,0,0,.35);z-index:2}
.hero-art{position:absolute;inset:0;background:radial-gradient(ellipse at 55% 45%,#8a3318 0%,#4a1a0c 45%,#140604 100%)}
.hero-title{position:absolute;right:80px;top:212px;font-family:"Jost",sans-serif;font-weight:400;font-size:43px;color:var(--white)}
.hero-sub{position:absolute;right:86px;top:280px;width:520px;text-align:right;font-family:"Jost",sans-serif;font-weight:300;font-size:21px;line-height:30px;color:var(--white)}
.hero-arrow{position:absolute;top:208px}

/* content panel */
.content{position:absolute;left:72px;top:696px;width:1056px;height:1530px;background:var(--panel)}
.section-title{position:absolute;left:0;width:1200px;text-align:center;font-family:"Jost",sans-serif;font-weight:300;font-size:45px;color:#666;line-height:1}
.section-title em{font-style:normal;color:var(--orange)}
.divider{position:absolute;left:0;width:1200px;height:20px}
.lead{position:absolute;left:195px;width:810px;text-align:center;font-size:16.5px;line-height:25px;color:var(--ink)}
.btn{position:absolute;background:var(--grey-btn);color:var(--white);font-family:"PT Sans",sans-serif;font-size:19px;display:flex;align-items:center;justify-content:center;border-left:5px solid var(--orange)}

.service-tabs{position:absolute;left:77px;top:1186px;width:1046px;height:126px;display:flex;gap:4px}
.service-tab{position:relative;flex:1;background:#f4f4f4;border:1px solid #d8d8d8;font-size:17px;color:#333;text-align:center}
.service-tab.active{background:#ececec;box-shadow:0 2px 4px rgba(0,0,0,.2)}
.service-tab span{position:absolute;left:0;right:0;bottom:16px;line-height:22px}
.tab-icon{position:absolute;left:50%;top:-44px;transform:translateX(-50%);width:82px;height:82px;border-radius:50%;background:var(--grey-icon);display:flex;align-items:center;justify-content:center}
.service-tab.active .tab-icon{background:var(--orange);box-shadow:0 0 0 10px rgba(240,90,40,.25)}
.tab-marker{position:absolute;left:50%;bottom:-16px;transform:translateX(-50%);width:30px;height:30px;border-radius:50%;background:var(--orange);display:flex;align-items:center;justify-content:center}

.advisory-photo{position:absolute;left:136px;top:1357px;width:312px;height:222px;background:linear-gradient(135deg,#c9d3e0,#8294ab 55%,#e8ecf1)}
.frame{position:absolute;border:1.5px solid #999}
.sub-title{position:absolute;font-family:"Jost",sans-serif;font-weight:400;font-size:29px;color:var(--orange)}
.copy{position:absolute;font-size:16px;line-height:29px;color:var(--ink)}
.copy p+p{margin-top:12px}

.product-art{position:absolute;left:682px;top:1723px;width:403px;height:455px;background:radial-gradient(ellipse at 55% 50%,#f05a28 0%,#e9b29c 45%,#f2f2f2 75%);border-radius:8px}

/* footer */
.contact{position:absolute;left:0;top:2226px;width:1200px;height:398px;background:var(--orange)}
.contact-title{position:absolute;left:0;top:40px;width:1200px;text-align:center;font-family:"Jost",sans-serif;font-weight:300;font-size:40px;color:var(--white)}
.field{position:absolute;background:var(--white);font-size:12px;color:#555;padding:6px 10px}
.contact-info{position:absolute;left:766px;font-size:13.5px;color:var(--white);line-height:22px}
.contact-info svg{position:absolute;left:0;top:2px}
.contact-info span{display:block;padding-left:28px}
.social{position:absolute;top:261px;width:46px;height:46px;border:2px solid var(--white);display:flex;align-items:center;justify-content:center}
.social i{width:12px;height:12px;border-radius:50%;background:var(--white)}
.footer-rule{position:absolute;left:110px;top:338px;width:980px;height:1px;background:rgba(255,255,255,.35)}
.copyright{position:absolute;left:0;top:358px;width:1200px;text-align:center;font-size:12.5px;color:var(--white)}
.copyright b{font-weight:400;color:#3a2a24}
</style>
</head>
<body>

<header class="site-header">
  <div class="brand"><div class="brand-dot"></div><div class="brand-name">Quantil Partners</div></div>
  <nav class="main-nav">
    <a class="active" href="#" style="left:635px">Home</a>
    <a href="#" style="left:717px">About Us</a>
    <a href="#" style="left:826px">Services</a>
    <a href="#" style="left:927px">Products</a>
    <a href="#" style="left:1039px">Contact Us</a>
  </nav>
  <div class="nav-underline"></div>
</header>

<section class="hero">
  <div class="hero-art" role="img" aria-label="Dark copper illustration of glowing molecular structures, flowing wave lines and stars"></div>
  <svg class="hero-arrow" style="left:24px" width="30" height="110" viewBox="0 0 30 110"><polyline points="26,2 4,55 26,108" fill="none" stroke="#bbb" stroke-width="2"/><polyline points="30,10 10,55 30,100" fill="none" stroke="#888" stroke-width="1"/></svg>
  <svg class="hero-arrow" style="left:1146px" width="30" height="110" viewBox="0 0 30 110"><polyline points="4,2 26,55 4,108" fill="none" stroke="#bbb" stroke-width="2"/><polyline points="0,10 20,55 0,100" fill="none" stroke="#888" stroke-width="1"/></svg>
  <h1 class="hero-title">Our company is DATA Science</h1>
  <p class="hero-sub">involved in development of software and professional service&nbsp; to larger enterprise clients</p>
</section>

<main class="content"></main>

<h2 class="section-title" style="top:762px">About <em>Quantil Partners</em></h2>
<svg class="divider" style="top:816px" viewBox="0 0 1200 20"><line x1="395" y1="10" x2="585" y2="10" stroke="#999"/><line x1="615" y1="10" x2="803" y2="10" stroke="#999"/><circle cx="600" cy="10" r="7" fill="none" stroke="#f05a28" stroke-width="1.5"/></svg>
<p class="lead" style="top:856px">We believe that every company needs data science and algorithms to stay on top of today's overwhelming speed of innovation. We advise and help to turn your company into a data driven company by making data science comprehensible and usable for everybody in your organization.</p>
<a class="btn" style="left:518px;top:945px;width:162px;height:50px">Read More</a>

<h2 class="section-title" style="top:1049px">What <em>We Do</em></h2>
<svg class="divider" style="top:1102px" viewBox="0 0 1200 20"><line x1="478" y1="10" x2="585" y2="10" stroke="#999"/><line x1="615" y1="10" x2="742" y2="10" stroke="#999"/><circle cx="600" cy="10" r="7" fill="none" stroke="#f05a28" stroke-width="1.5"/></svg>

<div class="service-tabs">
  <div class="service-tab active">
    <div class="tab-icon"><svg width="40" height="34" viewBox="0 0 40 34" fill="#fff"><circle cx="20" cy="9" r="5"/><circle cx="8" cy="13" r="4"/><circle cx="32" cy="13" r="4"/><path d="M12 30c0-6 4-10 8-10s8 4 8 10z"/><path d="M2 30c0-5 3-8 6-8s5 2 5 4v4z"/><path d="M38 30c0-5-3-8-6-8s-5 2-5 4v4z"/></svg></div>
    <span>Advisory</span>
    <div class="tab-marker"><svg width="14" height="14" viewBox="0 0 14 14" fill="none" stroke="#fff" stroke-width="2"><polyline points="2,2 7,6 12,2"/><polyline points="2,7 7,11 12,7"/></svg></div>
  </div>
  <div class="service-tab">
    <div class="tab-icon"><svg width="40" height="34" viewBox="0 0 40 34" fill="none" stroke="#fff" stroke-width="2.5"><rect x="3" y="3" width="34" height="22" rx="2"/><polyline points="8,20 15,12 21,17 31,8"/><line x1="14" y1="31" x2="26" y2="31"/></svg></div>
    <span>Insights</span>
  </div>
  <div class="service-tab">
    <div class="tab-icon"><svg width="40" height="40" viewBox="0 0 40 40" fill="none" stroke="#fff" stroke-width="3"><circle cx="18" cy="22" r="14"/><circle cx="18" cy="22" r="8"/><circle cx="18" cy="22" r="2" fill="#fff"/><line x1="18" y1="22" x2="34" y2="6"/></svg></div>
    <span>Targeting and<br>Optimization</span>
  </div>
  <div class="service-tab">
    <div class="tab-icon"><svg width="40" height="34" viewBox="0 0 40 34" fill="#fff"><path d="M2 8h12l3 4h15v18H2z"/><circle cx="30" cy="9" r="7" fill="#fff" stroke="#6f6f6f" stroke-width="2"/></svg></div>
    <span>Data Engineering</span>
  </div>
  <div class="service-tab">
    <div class="tab-icon"><svg width="40" height="40" viewBox="0 0 40 40" fill="none" stroke="#fff" stroke-width="2"><rect x="13" y="17" width="14" height="12" rx="1"/><path d="M16 17v-4a4 4 0 0 1 8 0v4"/><circle cx="6" cy="6" r="2"/><circle cx="34" cy="6" r="2"/><circle cx="6" cy="34" r="2"/><circle cx="34" cy="34" r="2"/><line x1="8" y1="8" x2="13" y2="17"/><line x1="32" y1="8" x2="27" y2="17"/><line x1="8" y1="32" x2="13" y2="29"/><line x1="32" y1="32" x2="27" y2="29"/></svg></div>
    <span>E-Privacy and security</span>
  </div>
</div>

<div class="frame" style="left:126px;top:1347px;width:135px;height:136px"></div>
<div class="frame" style="left:324px;top:1454px;width:136px;height:134px"></div>
<div class="advisory-photo" role="img" aria-label="Photo of a business team working together at a laptop, overlaid with a pale blue mosaic"></div>
<h3 class="sub-title" style="left:511px;top:1376px">Advisory</h3>
<div class="copy" style="left:511px;top:1428px;width:560px"><p>Data science comes in many flavors. Which one fits your company best? Taking all costs, benefits and organizational impact into account? We can help you with formulating a strategy to make sure you get the most out of your data.</p></div>

<h2 class="section-title" style="top:1643px">Our <em>Product</em></h2>
<svg class="divider" style="top:1695px" viewBox="0 0 1200 20"><line x1="458" y1="10" x2="585" y2="10" stroke="#999"/><line x1="615" y1="10" x2="742" y2="10" stroke="#999"/><circle cx="600" cy="10" r="7" fill="none" stroke="#f05a28" stroke-width="1.5"/></svg>

<h3 class="sub-title" style="left:110px;top:1775px">LUMORIA :</h3>
<div class="copy" style="left:110px;top:1826px;width:540px">
  <p>Lumoria is our on-demand, software-as-a-service real-time streaming data platform. You can use it to capture, analyze, profile and target your customers. The setup can be done in minutes, which prevents lengthy and costly implementation times. And all data will come in your own data warehouse.</p>
  <p>Lumoria is a combination of proven and disruptive technologies to ensure you work with the greatest in streaming and real-time. The 100% online reporting interface gives immediate access to the dashboards from any device or location.</p>
</div>
<div class="product-art" role="img" aria-label="Illustration of a desktop dashboard surrounded by floating browser windows, a phone and a paper plane"></div>

<footer class="contact">
  <h2 class="contact-title">Keep In Touch</h2>
  <svg class="divider" style="top:94px" viewBox="0 0 1200 20"><line x1="458" y1="10" x2="585" y2="10" stroke="rgba(255,255,255,.6)"/><line x1="615" y1="10" x2="742" y2="10" stroke="rgba(255,255,255,.6)"/><circle cx="600" cy="10" r="7" fill="none" stroke="#fff" stroke-width="1.5"/></svg>

  <form>
    <div class="field" style="left:122px;top:130px;width:210px;height:32px">Name</div>
    <div class="field" style="left:122px;top:172px;width:210px;height:32px">Emai id</div>
    <div class="field" style="left:122px;top:214px;width:210px;height:32px">Phn No</div>
    <div class="field" style="left:343px;top:130px;width:260px;height:116px">Message</div>
    <a class="btn" style="left:255px;top:252px;width:160px;height:49px;border-left-color:#555">Submit</a>
  </form>

  <div class="contact-info" style="top:138px"><svg width="16" height="22" viewBox="0 0 16 22" fill="#fff"><path d="M8 0a8 8 0 0 0-8 8c0 6 8 14 8 14s8-8 8-14a8 8 0 0 0-8-8zm0 11a3 3 0 1 1 0-6 3 3 0 0 1 0 6z"/></svg><span>48, Keizerskade Street,<br>Utrecht / The Netherlands, 3511 AB.</span></div>
  <div class="contact-info" style="top:196px"><svg width="18" height="18" viewBox="0 0 18 18" fill="#fff"><path d="M4 1l3 4-2 2c1 3 3 5 6 6l2-2 4 3-2 3C7 17 1 11 1 3z"/></svg><span>+31 20 555 0147</span></div>
  <div class="contact-info" style="top:232px"><svg width="18" height="14" viewBox="0 0 18 14" fill="#fff"><path d="M0 0h18v14H0z"/><path d="M0 0l9 7 9-7" fill="none" stroke="#f05a28" stroke-width="1.5"/></svg><span>hello@quantilpartners.com</span></div>

  <div class="social" style="left:764px"><i></i></div>
  <div class="social" style="left:815px"><i></i></div>
  <div class="social" style="left:868px"><i></i></div>

  <div class="footer-rule"></div>
  <p class="copyright">© <b>Quantil Partners</b> - 2017 All Right Reserved</p>
</footer>

</body>
</html>
```